Home Remodeling company needs a business card design

we need a business card design for home remodeling company in hamilton county, indiana USA. we offers a wide range of construction services including whole house renovations, Design and Build Basements and Kitchen and Bathroom Remodeling . we would like to see designs for both site of business card that use the same color of the company logo and also including all information below :
1- Samir Daoudi CEO / General Contractor
2- all company contacts Telephone numbers ( 1-888-TOVAL-42 ) ( 317-555-0192) email address ( info@tovalhome.example) website ( www.tovalhome.example ) and social media logos (Facebook- twitter- google plus )
3- company logo
4- licensed . insured . bonded

```html
<!DOCTYPE html>
<html lang="en">
<head>
<meta charset="utf-8">
<title>Toval Home Remodeling – Business Card</title>
<link rel="stylesheet" href="https://fonts.googleapis.com/css2?family=Open+Sans:wght@300;400;700&display=swap">
<style>
  :root {
    --backdrop: #3a3430;
    --card: #151515;
    --card-edge: #1f1f1f;
    --white: #f4f4f4;
    --soft: #c4c4c4;
    --red: #d9262b;
    --rule: #8a8a8a;
    --ink: #151515;
  }
  * { box-sizing: border-box; margin: 0; padding: 0; }
  html, body {
    width: 1200px; height: 787px; overflow: hidden;
    background: var(--backdrop);
    font-family: "Open Sans", Arial, sans-serif;
  }
  .stage {
    position: relative; width: 1200px; height: 787px;
    display: flex; align-items: center; justify-content: center; gap: 40px;
  }
  .card {
    position: relative; width: 540px; height: 309px;
    background: var(--card);
    border: 1px solid var(--card-edge);
    border-radius: 4px;
    box-shadow: 0 10px 30px rgba(0,0,0,.45);
    color: var(--white);
  }
  .company-name {
    font-weight: 700; font-size: 34px; line-height: 1.1;
    color: var(--white); white-space: nowrap;
  }

  /* back side */
  .card-back { display: flex; flex-direction: column; align-items: center; padding-top: 86px; }
  .card-back .company-name { color: var(--soft); }
  .credentials {
    margin-top: 30px; font-weight: 300; font-size: 16px; color: var(--white); letter-spacing: .5px;
  }
  .social-strip { margin-top: 14px; display: flex; align-items: center; gap: 8px; }
  .social-rule { width: 90px; height: 1px; background: linear-gradient(90deg, transparent, var(--rule)); }
  .social-rule.right { background: linear-gradient(90deg, var(--rule), transparent); }
  .social-icon {
    width: 20px; height: 20px; border-radius: 50%; background: var(--white);
    display: flex; align-items: center; justify-content: center;
  }
  .social-icon svg { width: 11px; height: 11px; fill: none; stroke: var(--ink); stroke-width: 2; stroke-linecap: round; stroke-linejoin: round; }

  /* front side */
  .card-front .company-name { position: absolute; right: 40px; top: 84px; }
  .person {
    position: absolute; left: 30px; top: 196px; text-align: right; width: 200px;
  }
  .person-name { color: var(--red); font-size: 18px; font-weight: 400; white-space: nowrap; }
  .person-title { color: var(--white); font-size: 14px; font-weight: 300; margin-top: 2px; white-space: nowrap; }
  .divider {
    position: absolute; left: 252px; top: 180px; width: 1px; height: 110px;
    background: linear-gradient(180deg, transparent, var(--rule), transparent);
  }
  .contacts { position: absolute; left: 270px; top: 184px; list-style: none; }
  .contacts li {
    display: flex; align-items: center; gap: 12px;
    font-size: 15px; font-weight: 400; color: var(--white); height: 22px; white-space: nowrap;
  }
  .contacts svg { width: 14px; height: 14px; fill: var(--red); flex: none; }
</style>
</head>
<body>
<main class="stage">

  <section class="card card-back" aria-label="Card back">
    <p class="company-name">Toval Home Remodeling</p>
    <p class="credentials">licensed | insured | bonded</p>
    <div class="social-strip" aria-label="Social media">
      <span class="social-rule"></span>
      <span class="social-icon" aria-label="Social link one">
        <svg viewBox="0 0 12 12" aria-hidden="true"><path d="M5 7l2-2M4 5.5L2.8 6.7a1.6 1.6 0 0 0 2.3 2.3L6.3 8M8 6.5l1.2-1.2a1.6 1.6 0 0 0-2.3-2.3L5.7 4"/></svg>
      </span>
      <span class="social-icon" aria-label="Social link two">
        <svg viewBox="0 0 12 12" aria-hidden="true"><path d="M2 2.5h8v5.5H5l-2.5 2V8H2z"/></svg>
      </span>
      <span class="social-icon" aria-label="Social link three">
        <svg viewBox="0 0 12 12" aria-hidden="true"><circle cx="3" cy="6" r="1.2"/><circle cx="9" cy="3" r="1.2"/><circle cx="9" cy="9" r="1.2"/><path d="M4.1 5.4l3.8-1.8M4.1 6.6l3.8 1.8"/></svg>
      </span>
      <span class="social-rule right"></span>
    </div>
  </section>

  <section class="card card-front" aria-label="Card front">
    <p class="company-name">Toval Home Remodeling</p>

    <div class="person">
      <p class="person-name">Samir Daoudi</p>
      <p class="person-title">CEO / General Contractor</p>
    </div>

    <span class="divider"></span>

    <ul class="contacts">
      <li>
        <svg viewBox="0 0 16 16" aria-hidden="true"><path d="M1 5c0-2 2-3 7-3s7 1 7 3v1h-4V4.5H5V6H1z M3 7h10l1 7H2z M8 9a2 2 0 1 0 0 4 2 2 0 0 0 0-4z"/></svg>
        1-888-TOVAL-42
      </li>
      <li>
        <svg viewBox="0 0 16 16" aria-hidden="true"><path d="M4 0h8a1 1 0 0 1 1 1v14a1 1 0 0 1-1 1H4a1 1 0 0 1-1-1V1a1 1 0 0 1 1-1zm1 2v10h6V2zm3 11a1 1 0 1 0 0 2 1 1 0 0 0 0-2z"/></svg>
        317-555-0192
      </li>
      <li>
        <svg viewBox="0 0 16 16" aria-hidden="true"><path d="M0 3h16v1L8 9 0 4z M0 6l8 5 8-5v7H0z"/></svg>
        info@tovalhome.example
      </li>
      <li>
        <svg viewBox="0 0 16 16" aria-hidden="true"><path d="M8 0a8 8 0 1 0 0 16A8 8 0 0 0 8 0zm0 3a3 3 0 1 1 0 6 3 3 0 0 1 0-6z"/></svg>
        www.tovalhome.example
      </li>
    </ul>
  </section>

</main>
</body>
</html>
```